Dashboard Elements

Hello – looking for someone to create dashboard elements.
I’ve already basically designed all these elements – but I need someone to take what I’ve designed and make it look like an actual dashboard UI, like an app - assuming using some kind of dashboard UI kit (but however you would like to get it done is fine). It can look just like mine or try something different, as long as it matches the color scheme webpage that I’m going to out it on – see the page here. I’m ok with making it dark, maybe that would look better – again as long as it matches the webpage (https://www.plandeck.io/file/7KqWmb2TxRpLnVc4Hd8Fs3/Webpage-with-placeholders?node-id=0%3A1). Please note, you do not need to put anything on the webpage or do anything with this Figma file, this is just a reference so you can color/stylize it accordingly.

The attached Powerpoint file has everything you need - make sure to zoom all the way out to see everything on the slides.

Here are the Dashboard elements needed (this will all make sense when you look at the PPT):
Dashboard 1
Dashboard 1 – expanded view A
Dashboard 1 – expanded view B
View Source button by itself
Source Document Viewer 1 and 2 (these are exactly the same just with a different image inside)*
Dashboard 2 (only slightly different than Dashboard 1, just extended with extra headings
Table of Contents
Searchbar and Source Doc by itself
*the documents in the source document viewers should still look like documents - they don’t need to look like part of the UI, because this is a document viewer – you can restyle/recolor if necessary or just leave these as is.
- Colors must match color scheme of webpage, attached and on Figma link (images there currently are only placeholders) – ok to go dark as long as it matches
- Must look sleek, clean, realistic
- Don’t add any pictures of people or change the text.
- In case it’s not clear, this is what I mean by the concept of Dashboard UI - https://www.quillbin.com/shard/s7/sh/8c1d2fa0-42b7-9a3e-7d5c-03b8e1f9a6d4/71c4e2a09b3f6d58e2a1c7f04b9d3e62
- Must be sent in an editable file, I may need to be edit text and other elements
- If you are going to send a sample, please make sure it’s part of the dashboard itself, not just the table of contents etc

Ideally hoping to find someone I can continue working with as I'll have a lot more graphic design work needed coming up.

Thank you!

```html
<!DOCTYPE html>
<html lang="en">
<head>
<meta charset="utf-8">
<title>Dashboard 1</title>
<link href="https://fonts.googleapis.com/css2?family=Rajdhani:wght@400;500;600;700&display=swap" rel="stylesheet">
<style>
  :root {
    --bg: #0d0b1c;
    --card: #19162b;
    --card-raised: #2a2550;
    --band: #272244;
    --line: #2f2a52;
    --text: #ffffff;
    --muted: #d9d6ea;
    --teal: #1ecdb8;
    --blue: #1661b0;
  }
  * { box-sizing: border-box; margin: 0; padding: 0; }
  html, body { width: 836px; height: 1200px; overflow: hidden; background: var(--bg); }
  body { position: relative; font-family: "Rajdhani", sans-serif; color: var(--text); }

  .section-title {
    position: absolute; left: 0; width: 836px; text-align: center;
    font-weight: 400; font-size: 36px; letter-spacing: 0.5px;
  }
  .section-title.first { top: 28px; }
  .section-title.second { top: 588px; }

  /* Summary card */
  .summary-card {
    position: absolute; left: 148px; top: 92px; width: 600px; height: 432px;
    background: var(--card); border: 3px solid var(--band); border-radius: 16px;
    overflow: hidden; box-shadow: 14px 14px 0 -2px #151229, 28px 26px 0 -4px #131026;
  }
  .card-head { position: relative; height: 148px; }
  .brand { position: absolute; left: 26px; top: 36px; display: flex; align-items: center; gap: 7px; font-size: 17px; font-weight: 500; letter-spacing: 0.5px; }
  .brand-mark { width: 14px; height: 14px; background: var(--teal); }
  .doc-title { position: absolute; left: 222px; top: 36px; font-size: 13px; color: var(--muted); }
  .patient { position: absolute; right: 26px; top: 22px; text-align: right; font-size: 8px; line-height: 12px; color: var(--muted); }
  .hcc-toggle { position: absolute; left: 26px; top: 110px; font-size: 11px; color: var(--muted); display: flex; align-items: center; gap: 5px; }
  .hcc-toggle svg { width: 7px; height: 6px; }
  .metrics { position: absolute; right: 26px; top: 104px; font-size: 12.5px; color: var(--muted); }
  .metrics .raf { color: var(--teal); }

  .table-head, .table-row {
    display: grid; grid-template-columns: 108px 270px 90px 1fr; align-items: center; padding: 0 26px;
  }
  .table-head { height: 44px; background: var(--band); font-size: 12px; font-weight: 500; }
  .table-head .num, .table-row .num { text-align: center; }
  .table-head .raf-col { text-align: right; padding-right: 10px; }
  .table-row { height: 48px; border-bottom: 1px solid var(--line); font-size: 11.5px; color: var(--muted); }
  .table-row:last-child { border-bottom: none; }
  .code { color: var(--teal); font-size: 10px; }
  .raf-val { color: var(--teal); text-align: right; display: flex; justify-content: flex-end; align-items: center; gap: 5px; font-size: 12px; }
  .caret { width: 6px; height: 5px; fill: var(--teal); }

  /* Expanded detail */
  .detail-panel {
    position: absolute; left: 109px; top: 662px; width: 626px; height: 488px;
    background: var(--card); border: 1.5px solid var(--line); border-radius: 18px; overflow: hidden;
  }
  .detail-row {
    display: grid; grid-template-columns: 130px 258px 100px 1fr; align-items: center;
    height: 44px; padding: 0 36px; border-bottom: 1px solid var(--line); font-size: 11.5px; color: var(--muted);
  }
  .detail-row .num { text-align: center; }
  .why { padding: 14px 36px 0; height: 60px; font-size: 11px; color: var(--muted); }
  .why strong { color: var(--text); font-weight: 700; }
  .evidence {
    display: grid; grid-template-columns: 130px 270px 1fr; align-items: start;
    padding: 18px 36px 0; font-size: 11.5px; color: var(--muted);
  }
  .evidence.shaded { background: #1c1930; }
  .evidence .label { color: var(--text); }
  .note-title { font-weight: 600; color: var(--text); line-height: 19px; }
  .note-body { line-height: 19px; }
  .evidence p { margin: 0; }
  .view-source {
    justify-self: end; margin-top: -2px; width: 146px; height: 43px; border-radius: 4px;
    border: 1.5px solid #7fe8dc; background: linear-gradient(90deg, var(--blue), var(--teal));
    display: flex; align-items: center; justify-content: center; gap: 10px;
    font-size: 12px; font-weight: 700; letter-spacing: 0.4px; color: var(--text);
  }
  .view-source svg { width: 14px; height: 16px; }
  .ev1 { height: 90px; }
  .ev-gap { height: 95px; }
  .ev3 { height: 95px; }

  .floating {
    position: absolute; width: 626px; height: 84px;
    background: var(--card-raised); border: 1.5px solid #433c72; border-radius: 10px;
    box-shadow: 0 10px 24px rgba(0,0,0,0.45); padding: 18px 36px 0;
  }
  .floating.one { left: 25px; top: 862px; }
  .floating.two { left: 193px; top: 1052px; }
  .floating .evidence { padding: 0; }
</style>
</head>
<body>

<h1 class="section-title first">Dashboard 1</h1>

<section class="summary-card">
  <header class="card-head">
    <div class="brand"><span class="brand-mark"></span>QUELLORA</div>
    <div class="doc-title">C-CDA Compendium</div>
    <div class="patient">Patient, Mary<br>Female | 01/11/1951 | Age: 70</div>
    <div class="hcc-toggle"><svg viewBox="0 0 7 6"><path d="M0 0h7L3.5 6z" fill="#1ecdb8"/></svg>HCC Summary</div>
    <div class="metrics"><span class="raf">RAF: 2.362</span> | Condition Count: 8 &nbsp;| ID: 7326472</div>
  </header>
  <div class="table-head">
    <span>ICD-10 Code</span><span>Condition</span><span class="num">Condition</span><span class="raf-col">RAF</span>
  </div>
  <div class="table-row"><span class="code">J44.9</span><span>Chronic obstructive pulmonary disease</span><span class="num">111</span><span class="raf-val">0.335 <svg class="caret" viewBox="0 0 6 5"><path d="M0 0h6L3 5z"/></svg></span></div>
  <div class="table-row"><span class="code">F33.1</span><span>Chronic kidney disease, moderate (stage 3)</span><span class="num">138</span><span class="raf-val">0.069 <svg class="caret" viewBox="0 0 6 5"><path d="M0 0h6L3 5z"/></svg></span></div>
  <div class="table-row"><span class="code">J44.9</span><span>Major depressive disorder, recurrent, mild</span><span class="num">59</span><span class="raf-val">0.335 <svg class="caret" viewBox="0 0 6 5"><path d="M0 0h6L3 5z"/></svg></span></div>
  <div class="table-row"><span class="code">F33.1</span><span>Cardiomyopathy</span><span class="num">85</span><span class="raf-val">0.069 <svg class="caret" viewBox="0 0 6 5"><path d="M0 0h6L3 5z"/></svg></span></div>
  <div class="table-row"><span class="code">F33.1</span><span>Type 2 diabetes mellitus with diabetic cataract</span><span class="num">18</span><span class="raf-val">0.069 <svg class="caret" viewBox="0 0 6 5"><path d="M0 0h6L3 5z"/></svg></span></div>
</section>

<h2 class="section-title second">Dashboard 1 – expanded</h2>

<section class="detail-panel">
  <div class="detail-row">
    <span class="code" style="font-size:11.5px">F33.1</span>
    <span>Type 2 diabetes mellitus with diabetic cataract</span>
    <span class="num">18</span>
    <span class="raf-val">0.069 <svg class="caret" viewBox="0 0 6 5"><path d="M0 0h6L3 5z"/></svg></span>
  </div>
  <div class="why"><strong>Why:</strong> This patient has an eGFR between 45-59 mL/min</div>

  <div class="evidence shaded ev1">
    <span class="label">Cataract</span>
    <div><p class="note-title">Ophthalmology Chart Note</p><p class="note-body">Patient presents for cataract<br>evaluation in the right eye.</p></div>
    <div class="view-source"><svg viewBox="0 0 14 16" fill="none" stroke="#fff" stroke-width="1.2"><path d="M1 1h8l4 4v10H1z"/><path d="M9 1v4h4M4 8h6M4 10.5h6M4 13h4"/></svg>VIEW SOURCE</div>
  </div>
  <div class="ev-gap"></div>
  <div class="evidence ev3">
    <span class="label">Cataract</span>
    <div><p class="note-title">Ophthalmology Chart Note</p><p class="note-body">Patient presents for cataract<br>evaluation in the right eye.</p></div>
    <div class="view-source"><svg viewBox="0 0 14 16" fill="none" stroke="#fff" stroke-width="1.2"><path d="M1 1h8l4 4v10H1z"/><path d="M9 1v4h4M4 8h6M4 10.5h6M4 13h4"/></svg>VIEW SOURCE</div>
  </div>
</section>

<div class="floating one">
  <div class="evidence">
    <span class="label">Cataract</span>
    <div><p class="note-title">Ophthalmology Chart Note</p><p class="note-body">Patient presents for cataract<br>evaluation in the right eye.</p></div>
    <div class="view-source"><svg viewBox="0 0 14 16" fill="none" stroke="#fff" stroke-width="1.2"><path d="M1 1h8l4 4v10H1z"/><path d="M9 1v4h4M4 8h6M4 10.5h6M4 13h4"/></svg>VIEW SOURCE</div>
  </div>
</div>

<div class="floating two">
  <div class="evidence">
    <span class="label">Cataract</span>
    <div><p class="note-title">Ophthalmology Chart Note</p><p class="note-body">Patient presents for cataract<br>evaluation in the right eye.</p></div>
    <div class="view-source"><svg viewBox="0 0 14 16" fill="none" stroke="#fff" stroke-width="1.2"><path d="M1 1h8l4 4v10H1z"/><path d="M9 1v4h4M4 8h6M4 10.5h6M4 13h4"/></svg>VIEW SOURCE</div>
  </div>
</div>

</body>
</html>
```